Brantley Oakhollow LLC. custom built/handcrafted

I am recent small business owner looking to sell my art(drawings) and woodworking projects from my home. I have a very rough draft of a simple card design created on a simple digital program. I was hoping for a fancier lettering on the initial letters (BO). More of a calligraphy style. Also, the yellow border around the logo I would like to be a gold foil look. For it to be shiny or reflective look and to keep the other letters black with a consistent font on the card and the card white.

Target Market(s)

Local and neighboring cities

Industry/Entity Type

Art (drawing)/Woodworking

Contact Information for Business Card

My email rpoakhollow@mailbright.net, phone number 617-530-4168. In the files provided it has a yellow border around the logo and I was looking to make that a gold foil.

Font styles to use
Serif
Decorative
Script

Requirements
Nice to have
• symbols for having a Facebook and Instagram

```html
<!DOCTYPE html>
<html lang="en">
<head>
<meta charset="UTF-8">
<title>Brantley Oakhollow LLC. – Business Card</title>
<link rel="stylesheet" href="https://fonts.googleapis.com/css2?family=Poppins:wght@400;500;600&display=swap">
<style>
  :root {
    --canvas-bg: #fdf4e6;
    --card-bg: #ffffff;
    --ink: #1a1a1a;
    --ink-soft: #2b2b2b;
    --gold: #c4913f;
    --gold-dark: #bd8a3a;
    --gold-light: #f3dc95;
    --shadow: rgba(120, 90, 40, 0.10);
  }
  * { box-sizing: border-box; margin: 0; padding: 0; }
  html, body { width: 1006px; height: 1200px; overflow: hidden; }
  body {
    background: var(--canvas-bg);
    font-family: "Poppins", sans-serif;
    color: var(--ink);
    position: relative;
  }
  .card {
    position: absolute;
    left: 61px;
    width: 883px;
    height: 505px;
    background: var(--card-bg);
    box-shadow: 0 2px 10px var(--shadow);
  }
  .card--front { top: 66px; }
  .card--back { top: 621px; }

  .foil-frame {
    position: absolute;
    border: 4px solid transparent;
    border-image: linear-gradient(135deg, var(--gold-dark) 0%, var(--gold-light) 45%, var(--gold) 60%, var(--gold-light) 80%, var(--gold-dark) 100%) 1;
    background: linear-gradient(160deg, rgba(240,240,240,0.35) 0%, rgba(255,255,255,0) 55%);
  }
  .card--front .foil-frame { left: 58px; top: 60px; width: 766px; height: 384px; }
  .card--back .foil-frame { left: 27px; top: 37px; width: 828px; height: 430px; }

  .brand-name {
    position: absolute;
    left: 0; right: 0;
    top: 180px;
    text-align: center;
    font-weight: 600;
    font-size: 46px;
    letter-spacing: 0.5px;
    color: var(--ink);
  }
  .tagline {
    position: absolute;
    left: 0; right: 0;
    top: 388px;
    text-align: center;
    font-size: 23.5px;
    font-weight: 400;
    color: var(--ink-soft);
  }

  .holder-name {
    position: absolute;
    left: 71px;
    top: 194px;
    font-size: 30px;
    font-weight: 600;
    letter-spacing: 0.3px;
  }
  .holder-role {
    position: absolute;
    left: 71px;
    top: 244px;
    font-size: 22.5px;
    font-weight: 500;
    color: var(--gold);
    letter-spacing: 0.5px;
  }
  .social {
    position: absolute;
    left: 71px;
    top: 297px;
    display: flex;
    gap: 8px;
  }
  .social__ring {
    width: 54px; height: 54px;
    border: 1.5px solid var(--gold);
    border-radius: 50%;
  }

  .contact-list {
    position: absolute;
    left: 450px;
    top: 172px;
    list-style: none;
  }
  .contact-item {
    display: flex;
    align-items: center;
    height: 45px;
    margin-bottom: 20px;
  }
  .contact-icon {
    flex: none;
    width: 45px; height: 45px;
    border-radius: 50%;
    background: var(--gold);
    display: flex;
    align-items: center;
    justify-content: center;
    margin-right: 23px;
  }
  .contact-text { font-size: 22px; color: var(--ink-soft); }
  .contact-text--address { font-size: 18px; line-height: 1.15; margin-top: -12px; }
</style>
</head>
<body>

  <section class="card card--front">
    <div class="foil-frame"></div>
    <p class="brand-name">Brantley Oakhollow</p>
    <p class="tagline">CUSTOM BUILT - HANDCRAFTED</p>
  </section>

  <section class="card card--back">
    <div class="foil-frame"></div>
    <p class="holder-name">REID P.OAKHOLLOW</p>
    <p class="holder-role">OWNER</p>
    <div class="social">
      <span class="social__ring" aria-label="Social profile"></span>
      <span class="social__ring" aria-label="Social profile"></span>
    </div>

    <ul class="contact-list">
      <li class="contact-item">
        <span class="contact-icon">
          <svg width="14" height="18" viewBox="0 0 14 18" aria-hidden="true">
            <path d="M7 0C3.1 0 0 3 0 6.8 0 11.8 7 18 7 18s7-6.2 7-11.2C14 3 10.9 0 7 0zm0 9.3a2.5 2.5 0 1 1 0-5 2.5 2.5 0 0 1 0 5z" fill="#fff"/>
          </svg>
        </span>
        <span class="contact-text contact-text--address">256 Lorem Ipsum Dummy text<br>Lorem Ipsum</span>
      </li>
      <li class="contact-item">
        <span class="contact-icon">
          <svg width="18" height="13" viewBox="0 0 18 13" aria-hidden="true">
            <rect x="0.5" y="0.5" width="17" height="12" rx="1" fill="#fff"/>
            <path d="M1 1.2 9 7.5l8-6.3" fill="none" stroke="#c4913f" stroke-width="1.3"/>
          </svg>
        </span>
        <span class="contact-text">rpoakhollow@mailbright.net</span>
      </li>
      <li class="contact-item">
        <span class="contact-icon">
          <svg width="18" height="18" viewBox="0 0 24 24" aria-hidden="true">
            <path d="M6.6 10.8a15.1 15.1 0 0 0 6.6 6.6l2.2-2.2a1 1 0 0 1 1-.25 11.4 11.4 0 0 0 3.6.57 1 1 0 0 1 1 1V20a1 1 0 0 1-1 1A17 17 0 0 1 3 4a1 1 0 0 1 1-1h3.5a1 1 0 0 1 1 1c0 1.25.2 2.45.57 3.57a1 1 0 0 1-.25 1z" fill="#fff"/>
          </svg>
        </span>
        <span class="contact-text">617-530-4168</span>
      </li>
    </ul>
  </section>

</body>
</html>
```